3 -4 PAGE GIFT CERTIFICATE REDEMPTION WEBSITE REVAMP

I am revamping the entire website at www.brightperkcentral.net

Will have brand new theme and new logo. Name Of Company:
Bonus Gratuity Dispatch Network
BGDN

OVERVIEW:
I NEED A 3-4 PAGE WEBSITE DESIGNED WITH CHECKOUT MODULE.
My company offers fully brandable and personalizable gift certificates good for travel, vacations, dining rewards, rebates, electronic gifts, etc. and I need to redesign the website where the fulfillment and redemption happens.

So the way it works is a business uses my online platform to create, brand and personalize these gift certificates. The business can brand the certificates in the upper right hand corner of each certificate where the “Compliments Of” area sits with their company logo, website, contact info, etc and can also personalize each individual gift certificate to a specific customer too. SEE EXAMPLE ATTACHED TO BRIEF.

The example I attached to this brief includes a logo which is really just a picture and under it there is 3 lines of text where the business can put a website, phone number and email.

On the left side of the top banner image you will see “Exclusively For”.

So now, after a customer enters their certificate ID #, the branding on the next page must match the Compliments Of area and also must personalize the Sales Page to the customer that is in the Exclusively For” area of the certificate…...

Page 1: LANDING PAGE
CONTENT:

Welcome to the online redemption source for vacation certificates, travel vouchers, digital electronic products, dining incentives, gas and grocery rewards and more!

ENTER YOUR CERTIFICATE ID #
ENTER YOUR EMAIL

Welcome to the online redemption system for vacation certificates, travel vouchers, rebates, digital products, dining incentives, gas and grocery rewards and more!

PLEASE ENTER A VALID CERTIFICATE ID NUMBER TO VIEW THE DETAILS AND TO REDEEM AND ACTIVATE YOUR SPECIAL OFFER.

Also we need a testimonial module ON THIS PAGE AND SALES PAGE

PAGE 2: SALES PAGE FOR OFFER (we will use the 1-4 Night Las Vegas Hotel Stay Certificate)
INSTRUCTIONS EXPLANATION FOR DESIGNER: Every gift certificate has a "Compliments Of Area" in the upper right hand corner....SEE SAMPLE ATTACHED TO BRIEF. On the sales page we also show this to the customer after they enter the code. Every certificate has a Compliments Of area and we will also add "Exclusively For" so the person that is giving the certificate away can specify the name of the recipient so we will also transffer this information over to the SALES PAGE.

CONTENT FOR SALES PAGE:

WELCOME ~~NAME OF PERSON IN EXCLUSIVELY FOR AREA ON CERTIFICATE~~ !!

THIS SPECIAL INCENTIVE OFFER IS COMPLIMENTS OF

~~LOGO THAT IS SEEN ON CERTIFICATE~~
~~TEXT LINE 1~~
~~TEXT LINE 2~~
~~TEXT LINE 3~~

TITLE OF OFFER: STAY & PLAY IN LAS VEGAS FOR UP TO 4 NIGHTS!
There is no doubt that Las Vegas is one of the hottest travel destinations around the world. In fact, some people would even go as far as saying that perhaps it is THE hottest place to visit. Enjoy up to 4 nights of resort/casino accommodations in exciting Las Vegas, NV. Millions of people travel to this exciting city each year to enjoy its thrills. Thanks to the business you received this certificate from, now you can enjoy Las Vegas, NV too!

Features:
*Travel 7 Days A Week
*Stay Your Choice Of Nights (1-4 Nights)
*Good For Two Adults & Two Children
*Pay Just The Taxes & Fees
*Multiple Travel Date Requests Allowed
*Fully Transferable To Another Person
*Just A 30 Days Advance Notice Required
*You Will Have 12 Months To Complete Travel

HOW CAN WE DO THIS?

We contract with the world leading hotel chains and resorts to help them fill their otherwise empty rooms.

We help fill empty rooms which the hotels, resorts and cruise lines turn into additional revenue from other areas of their property and future bookings.

Hotels rarely experience full occupancy, yet they remain open, providing rooms and services at fixed costs. So when hotels give out their rooms by partnering with marketing companies like us, they might miss out on the room fee, but they already didn't have that in the first place, at least now they have the opportunity to gain a customer for their in-house restaurants, room service, their casinos, an extra day stay, future bookings, etc.

The magic of why our program works so well is the fact that it’s a win win for everyone involved. You win because you received a huge savings. The business who gave you the certificate wins because now you will remember them the next time you need the same kind of product or service that they provide and you might even refer your friends and family members. The hotels and resorts win because they gain additional revenue from other areas of their establishment that they otherwise would not have been able to get and they also have a new client that may book with them in the future. Remember, they didn’t have anyone in the room in the first place so since you are paying the normal rack rate you might be more inclined to spend your money at the hotel. You are never under any obligation to do so though!

Retail Value: Up to $826.00 (based on $159.00 per night)

How it Works:
You will receive up to 4 nights in a 3 star or better Las Vegas resort and casino for up to 4 travelers, 2 adults and 2 children.

Simply redeem the certificate to activate the travel period for 1 year. This means you will have at least 1 year to travel from the date you redeem and activate your offer. Be sure to redeem your certificate before it expires! All certificates will have an accompanying expiration date attached to them.

When you are ready to book you will simply have to pay the daily room rate taxes and fees of approximately $12-$33 per night (not per person). On average the taxes and fees come out to about $19 per night. (Retail Value: Up to $826.00 based on $159.00 per night)

Step 1: Redeem your certificate to activate your offer

Step 2: Fill out the online reservation request form with travel dates within the next 12 months.

Step 3: Wait for a confirmation of your booked reservation. You will be notified immediately upon us booking your reservation.

Go on your vacation and thank the business who gave you this special offer by doing business with them again and referring your friends and family members!

No timeshares or sales presentations, Guaranteed!

PAGE 3 IS CHECKOUT PAGE:

PLEASE USE ****HERE IS SAMPLE CODE FOR YOU TO TEST OUT AT CURRENT REDEMPTION PROCESS WWW.BRIGHTPERKCENTRAL.NET 40613-27149

TO SEE THE CURRENT CHECK OUT. I NEED ALL THE SAME CONTENT JUST A DIFFERENT MORE EFFICIENT CHECKOUT PROCESS HERE. OMIT THE LEFT SIDE OF THE CURRENT CHECK OUT PROCESS AS THIS CURRENT PROCESSS IS ONE STEP AND DOES NOT HAVE A SALES PAGE BUT NOW I AM CREATING A SALES PAGE BEFORE THE CHECKOUT SO THE BRANDING AND PERSONALIZATION WILL HAPPEN ON THE SALES PAGE….THANK YOU

Target Market(s)

END USERS THAT ARE REDEEMING SPECIAL OFFERS GIFT CERTIFICATES

Industry/Entity Type

Marketing

Number of Pages Required

4 page

Colors

Designer to choose colors to be used in the design.

Requirements
Must have
• OVERVIEW:
• I NEED A 3-4 PAGE WEBSITE DESIGNED WITH CHECKOUT MODULE.
• My company offers fully brandable and personalizable gift certificates good for travel, vacations, dining rewards, rebates, electronic gifts, etc. and I need to redesign the website where the fulfillment and redemption happens.
• So the way it works is a business uses my online platform to create, brand and personalize these gift certificates. The business can brand the certificates in the upper right hand corner of each certificate where the “Compliments Of” area sits with their company logo, website, contact info, etc and can also personalize each individual gift certificate to a specific customer too. SEE EXAMPLE ATTACHED TO BRIEF.
• The example I attached to this brief includes a logo which is really just a picture and under it there is 3 lines of text where the business can put a website, phone number and email.
• On the left side of the top banner image you will see “Exclusively For”.
• So now, after a customer enters their certificate ID #, the branding on the next page must match the Compliments Of area and also must personalize the Sales Page to the customer that is in the Exclusively For” area of the certificate…...
• Page 1: LANDING PAGE
• CONTENT:
• Welcome to the online redemption source for vacation certificates, travel vouchers, digital electronic products, dining incentives, gas and grocery rewards and more!
• ENTER YOUR CERTIFICATE ID #
• ENTER YOUR EMAIL
• Welcome to the online redemption system for vacation certificates, travel vouchers, rebates, digital products, dining incentives, gas and grocery rewards and more!
• PLEASE ENTER A VALID CERTIFICATE ID NUMBER TO VIEW THE DETAILS AND TO REDEEM AND ACTIVATE YOUR SPECIAL OFFER.
• Also we need a testimonial module ON THIS PAGE AND SALES PAGE
• PAGE 2: SALES PAGE FOR OFFER (we will use the 1-4 Night Las Vegas Hotel Stay Certificate)
• INSTRUCTIONS EXPLANATION FOR DESIGNER: Every gift certificate has a "Compliments Of Area" in the upper right hand corner....SEE SAMPLE ATTACHED TO BRIEF. On the sales page we also show this to the customer after they enter the code. Every certificate has a Compliments Of area and we will also add "Exclusively For" so the person that is giving the certificate away can specify the name of the recipient so we will also transffer this information over to the SALES PAGE.
• CONTENT FOR SALES PAGE:
• WELCOME ~~NAME OF PERSON IN EXCLUSIVELY FOR AREA ON CERTIFICATE~~ !!
• THIS SPECIAL INCENTIVE OFFER IS COMPLIMENTS OF
• ~~LOGO THAT IS SEEN ON CERTIFICATE~~
• ~~TEXT LINE 1~~
• ~~TEXT LINE 2~~
• ~~TEXT LINE 3~~
• TITLE OF OFFER: STAY & PLAY IN LAS VEGAS FOR UP TO 4 NIGHTS!
• There is no doubt that Las Vegas is one of the hottest travel destinations around the world. In fact, some people would even go as far as saying that perhaps it is THE hottest place to visit. Enjoy up to 4 nights of resort/casino accommodations in exciting Las Vegas, NV. Millions of people travel to this exciting city each year to enjoy its thrills. Thanks to the business you received this certificate from, now you can enjoy Las Vegas, NV too!
• Features:
• *Travel 7 Days A Week
• *Stay Your Choice Of Nights (1-4 Nights)
• *Good For Two Adults & Two Children
• *Pay Just The Taxes & Fees
• *Multiple Travel Date Requests Allowed
• *Fully Transferable To Another Person
• *Just A 30 Days Advance Notice Required
• *You Will Have 12 Months To Complete Travel
• HOW CAN WE DO THIS?
• We contract with the world leading hotel chains and resorts to help them fill their otherwise empty rooms.
• We help fill empty rooms which the hotels, resorts and cruise lines turn into additional revenue from other areas of their property and future bookings.
• Hotels rarely experience full occupancy, yet they remain open, providing rooms and services at fixed costs. So when hotels give out their rooms by partnering with marketing companies like us, they might miss out on the room fee, but they already didn't have that in the first place, at least now they have the opportunity to gain a customer for their in-house restaurants, room service, their casinos, an extra day stay, future bookings, etc.
• The magic of why our program works so well is the fact that it’s a win win for everyone involved. You win because you received a huge savings. The business who gave you the certificate wins because now you will remember them the next time you need the same kind of product or service that they provide and you might even refer your friends and family members. The hotels and resorts win because they gain additional revenue from other areas of their establishment that they otherwise would not have been able to get and they also have a new client that may book with them in the future. Remember, they didn’t have anyone in the room in the first place so since you are paying the normal rack rate you might be more inclined to spend your money at the hotel. You are never under any obligation to do so though!
• Retail Value: Up to $826.00 (based on $159.00 per night)
• How it Works:
• You will receive up to 4 nights in a 3 star or better Las Vegas resort and casino for up to 4 travelers, 2 adults and 2 children.
• Simply redeem the certificate to activate the travel period for 1 year. This means you will have at least 1 year to travel from the date you redeem and activate your offer. Be sure to redeem your certificate before it expires! All certificates will have an accompanying expiration date attached to them.
• When you are ready to book you will simply have to pay the daily room rate taxes and fees of approximately $12-$33 per night (not per person). On average the taxes and fees come out to about $19 per night. (Retail Value: Up to $826.00 based on $159.00 per night)
• Step 1: Redeem your certificate to activate your offer
• Step 2: Fill out the online reservation request form with travel dates within the next 12 months.
• Step 3: Wait for a confirmation of your booked reservation. You will be notified immediately upon us booking your reservation.
• Go on your vacation and thank the business who gave you this special offer by doing business with them again and referring your friends and family members!
• No timeshares or sales presentations, Guaranteed!
• PAGE 3 IS CHECKOUT PAGE:
• PLEASE USE ****HERE IS SAMPLE CODE FOR YOU TO TEST OUT AT CURRENT REDEMPTION PROCESS WWW.BRIGHTPERKCENTRAL.NET 40613-27149
• TO SEE THE CURRENT CHECK OUT. I NEED ALL THE SAME CONTENT JUST A DIFFERENT MORE EFFICIENT CHECKOUT PROCESS HERE. OMIT THE LEFT SIDE OF THE CURRENT CHECK OUT PROCESS AS THIS CURRENT PROCESSS IS ONE STEP AND DOES NOT HAVE A SALES PAGE BUT NOW I AM CREATING A SALES PAGE BEFORE THE CHECKOUT SO THE BRANDING AND PERSONALIZATION WILL HAPPEN ON THE SALES PAGE….THANK YOU
Nice to have
• OVERVIEW:
• Page 1: LANDING PAGE
• CONTENT:
• ENTER YOUR EMAIL
• CONTENT FOR SALES PAGE:
• ~~TEXT LINE 1~~
• ~~TEXT LINE 2~~
• ~~TEXT LINE 3~~
• Features:
• *Travel 7 Days A Week
• HOW CAN WE DO THIS?
• How it Works:
Should not have
• OVERVIEW:
• Page 1: LANDING PAGE
• CONTENT:
• ENTER YOUR EMAIL
• CONTENT FOR SALES PAGE:
• ~~TEXT LINE 1~~
• ~~TEXT LINE 2~~
• ~~TEXT LINE 3~~
• Features:
• *Travel 7 Days A Week
• HOW CAN WE DO THIS?
• How it Works:

```html
<!DOCTYPE html>
<html lang="en">
<head>
<meta charset="utf-8">
<title>Bonus Gratuity Dispatch Network – Sales Page</title>
<link href="https://fonts.googleapis.com/css2?family=Jost:wght@400;500;600&family=Roboto+Condensed:wght@400;500;700&display=swap" rel="stylesheet">
<style>
:root{
  --yellow:#fbb829;
  --yellow-deep:#f6a21a;
  --orange:#f47421;
  --navy:#0c2d4e;
  --maroon:#2d0306;
  --grey:#efefef;
  --ink:#2a1a14;
  --rule:#8a6a55;
  --white:#ffffff;
}
*{margin:0;padding:0;box-sizing:border-box}
html,body{width:1200px;height:4861px;overflow:hidden}
body{position:relative;background:var(--white);font-family:"Jost",sans-serif;color:var(--ink)}
.abs{position:absolute}
.cond{font-family:"Roboto Condensed",sans-serif}
.ph{position:absolute}

/* header & hero */
.hero{position:absolute;left:0;top:0;width:1200px;height:1043px;background:var(--yellow);overflow:hidden}
.topbar{position:absolute;left:0;top:0;width:800px;height:68px;background:var(--white);border-bottom-right-radius:60px 68px}
.brand{position:absolute;left:157px;top:8px;font-family:"Roboto Condensed",sans-serif;font-weight:700;font-size:22px;line-height:21px;color:var(--navy)}
.nav{position:absolute;top:88px;left:0;font-size:13px;color:var(--ink)}
.nav a{position:absolute;white-space:nowrap;text-decoration:none;color:var(--ink)}
.nav a.active{border-bottom:1px solid var(--ink);padding-bottom:12px}
.hero-photo{left:0;top:128px;width:1140px;height:360px;border-radius:0 90px 140px 0;background:linear-gradient(180deg,#9cc6e4 0%,#d7dde0 35%,#c7b79b 60%,#5d9fb4 100%)}
.blob{position:absolute;background:var(--yellow)}
.cert{left:785px;top:0;width:258px;height:244px;background:var(--white);box-shadow:0 4px 12px rgba(0,0,0,.15);text-align:center;padding-top:6px}
.cert h4{font-family:"Jost",sans-serif;font-weight:600;color:var(--orange);font-size:14px;line-height:18px;letter-spacing:.5px}
.cert .logo-ph{margin:6px auto 0;width:186px;height:82px;background:linear-gradient(180deg,#b7d3ea,#c9b48e)}
.cert .courtesy{font-size:12px;margin-top:8px;color:var(--ink)}
.cert .line{font-size:12px;line-height:20px;display:flex;justify-content:center;align-items:center;gap:5px}
.excl{left:253px;top:458px;width:744px;height:61px;background:var(--orange);color:var(--white);font-size:22px;letter-spacing:1px;padding:16px 0 0 84px}
.offer-bar{left:253px;top:523px;width:790px;height:100px}
.offer-bar span{position:absolute;left:82px;top:26px;color:var(--white);font-weight:500;font-size:37px;letter-spacing:2px}
.offer-head{left:0;top:670px;width:1200px;text-align:center}
.offer-head h2{font-family:"Roboto Condensed",sans-serif;font-weight:400;font-size:32px;color:var(--ink)}
.offer-head .rule{width:240px;height:1px;background:var(--rule);margin:6px auto 0}
.offer-head h1{font-family:"Jost",sans-serif;font-weight:500;font-size:31px;margin-top:12px;letter-spacing:.5px}
.offer-head p{width:730px;margin:4px auto 0;font-size:14px;line-height:19.5px}
.skyline{left:0;top:870px;width:1200px;height:173px;background:linear-gradient(180deg,rgba(255,255,255,0) 0%,rgba(231,196,140,.55) 55%,#e9d2ad 100%)}

/* features */
.feat-photo{left:157px;top:1130px;width:451px;height:356px;background:linear-gradient(180deg,#4ea8de 0%,#7cc5e8 40%,#1e88b8 60%,#3b6b4a 85%,#dcd8cf 100%)}
.h3{font-family:"Roboto Condensed",sans-serif;font-weight:500;font-size:32px;color:var(--ink)}
.bullets{list-style:none}
.bullets li{position:relative;padding-left:25px;font-size:14.5px;line-height:28.5px}
.bullets li::before{content:"";position:absolute;left:0;top:12px;width:5px;height:5px;border-radius:50%;background:var(--ink)}

/* how can we */
.maroon{left:0;top:1566px;width:1200px;height:542px;background:var(--maroon);color:var(--white)}
.maroon .title{position:absolute;left:0;top:76px;width:1200px;text-align:center;font-family:"Roboto Condensed",sans-serif;font-size:32px}
.maroon .title::after{content:"";display:block;width:312px;height:1px;background:#9c7b76;margin:8px auto 0}
.mlist{position:absolute;list-style:none;font-size:12.5px;line-height:19px}
.mlist li{position:relative;padding-left:25px;margin-bottom:20px}
.mlist li::before{content:"";position:absolute;left:0;top:7px;width:5px;height:5px;border-radius:50%;background:var(--white)}
.vrule{left:600px;top:158px;width:1px;height:352px;background:#6d4b47}
.retail{left:206px;top:2057px;width:785px;height:100px;color:var(--white);text-align:center}
.retail .big{position:absolute;left:0;top:20px;width:735px;font-weight:500;font-size:31px;letter-spacing:1px;line-height:34px}
.retail .small{position:absolute;left:0;top:55px;width:735px;font-weight:500;font-size:22px;letter-spacing:1px}

/* how it works */
.hiw-photo{left:157px;top:2223px;width:436px;height:404px;background:linear-gradient(180deg,#6f93b7 0%,#a8b9c9 35%,#5a4a3c 50%,#3d7da4 70%,#1e5f88 100%)}
.hiw li{position:relative;padding-left:16px;font-size:13px;line-height:19.3px;margin-bottom:16px;list-style:none}
.hiw li::before{content:"";position:absolute;left:0;top:7px;width:5px;height:5px;border-radius:50%;background:var(--ink)}

/* testimonials */
.testi{left:0;top:2689px;width:1200px;height:561px;background:var(--grey)}
.testi .title{position:absolute;top:70px;width:1200px;text-align:center}
.testi .title span{font-family:"Roboto Condensed",sans-serif;font-weight:500;font-size:32px;display:inline-block;border-bottom:1px solid var(--rule);padding:0 4px 6px}
.card{position:absolute;background:var(--white);font-size:12.5px;line-height:19px;padding:18px 22px;box-shadow:0 2px 6px rgba(0,0,0,.05)}
.card::after{content:"";position:absolute;left:30px;bottom:-18px;border-left:0 solid transparent;border-right:28px solid transparent;border-top:18px solid var(--white)}
.who{position:absolute;font-size:12.5px;line-height:16px}
.who b{font-weight:500;color:var(--navy);letter-spacing:.5px}
.dots{position:absolute;left:584px;top:3219px;display:flex;gap:6px}
.dots i{width:6px;height:6px;border-radius:50%;border:1px solid var(--navy)}
.dots i.on{background:var(--navy)}

/* video */
.sell-title{left:0;top:3322px;width:1200px;text-align:center;font-family:"Roboto Condensed",sans-serif;font-weight:500;font-size:34px}
.video{left:162px;top:3387px;width:876px;height:400px;border:5px solid var(--white);box-shadow:0 2px 10px rgba(0,0,0,.25);background:linear-gradient(180deg,#a9cbe5 0%,#d6e2ea 40%,#8c9a7a 65%,#5fb7cf 82%,#c7c2bb 100%)}
.play{left:551px;top:3540px;width:96px;height:96px;border-radius:50%;background:rgba(255,255,255,.45)}

/* steps */
.steps{left:0;top:3821px;width:1200px;height:398px;background:linear-gradient(135deg,var(--yellow) 0%,var(--yellow-deep) 50%,var(--yellow) 100%)}
.step{position:absolute;top:115px;width:280px;text-align:center}
.step .n{font-family:"Jost",sans-serif;font-weight:600;font-size:78px;line-height:80px;color:var(--ink)}
.step p{font-size:14px;line-height:22px;margin-top:14px}

.closing{left:0;top:4283px;width:1200px;text-align:center}
.closing p{font-size:20px;line-height:28px;width:860px;margin:0 auto}
.closing h3{font-weight:500;font-size:29px;letter-spacing:1.5px;margin-top:20px;line-height:36px}
.closing h2{font-weight:600;font-size:38px;letter-spacing:1.5px;line-height:44px}

/* footer */
.footer{left:0;top:4487px;width:1200px;height:374px;background:var(--navy);color:var(--white)}
.fcol{position:absolute;top:95px;font-size:12.5px;line-height:19px}
.fcol h5{font-family:"Roboto Condensed",sans-serif;font-weight:500;font-size:17px;margin-bottom:22px}
.frule{left:157px;top:272px;width:886px;height:1px;background:#35506c}
.copy{left:0;top:316px;width:1200px;text-align:center;font-size:12px}
</style>
</head>
<body>

<section class="hero">
  <div class="ph hero-photo" role="img" aria-label="Aerial photo of the Las Vegas Strip with resort towers and a lake"></div>
  <svg class="abs" style="left:0;top:0" width="1200" height="1043" viewBox="0 0 1200 1043" aria-hidden="true">
    <path d="M0 128 L0 360 Q40 240 20 128 Z" fill="#fbb829"/>
    <path d="M1040 128 Q1160 130 1140 220 Q1130 300 1200 330 L1200 0 L1040 0 Z" fill="#fbb829"/>
    <path d="M0 470 L1200 470 L1200 380 Q1140 470 960 470 Q700 470 500 470 Q200 470 0 440 Z" fill="#fbb829"/>
  </svg>
  <div class="topbar"></div>
  <div class="brand">Bonus Gratuity<br>Dispatch Network</div>
  <nav class="nav">
    <a style="left:181px">Home</a>
    <a class="active" style="left:268px">Sales page For Offer</a>
    <a style="left:449px">Checkout Page</a>
  </nav>
  <div class="abs cert">
    <h4>THIS CERTIFICATE IS<br>COMPLIMENTS OF</h4>
    <div class="logo-ph" role="img" aria-label="Business logo image"></div>
    <div class="courtesy">Certificate Courtesy Of</div>
    <div class="line"><svg width="11" height="9" viewBox="0 0 11 9"><rect x=".5" y=".5" width="10" height="8" fill="none" stroke="#2a1a14"/><path d="M.5 .5 L5.5 5 L10.5 .5" fill="none" stroke="#2a1a14"/></svg>hello@sunpathgifts.com</div>
    <div class="line"><svg width="9" height="11" viewBox="0 0 9 11"><path d="M2 1 L4 1 L4 4 L3 5 Q4 7 6 8 L7 7 L9 8 L9 10 Q4 11 1 5 Q0 3 2 1Z" fill="#2a1a14"/></svg>555-204-318</div>
    <div class="line"><svg width="11" height="11" viewBox="0 0 11 11"><circle cx="5.5" cy="5.5" r="5" fill="none" stroke="#2a1a14"/><path d="M.5 5.5 H10.5 M5.5 .5 V10.5" stroke="#2a1a14" fill="none"/></svg>http://sunpathgifts.com</div>
  </div>
  <div class="abs excl">EXCLUSIVE FOR : LOREM IPSUM</div>
  <div class="abs offer-bar">
    <svg width="790" height="100" viewBox="0 0 790 100" aria-hidden="true"><polygon points="0,0 745,0 790,50 745,100 0,100" fill="#0c2d4e"/></svg>
    <span>AIRFARE &amp; HOTEL FOR TWO</span>
  </div>
  <div class="abs offer-head">
    <h2>OUR OFFER</h2>
    <div class="rule"></div>
    <h1>STAY &amp; PLAY IN LAS VEGAS FOR UP TO 4 NIGHTS!</h1>
    <p>There is no doubt that Las Vegas is one of the hottest travel destinations around the world. In fact, some people would even go as far as saying that perhaps it is THE hottest place to visit. Enjoy up to 4 nights of resort/casino accommodations in exciting Las Vegas, NV. Millions of people travel to this exciting city each year to enjoy its thrills. Thanks to the business you received this certificate from, now you can enjoy Las Vegas, NV too!</p>
  </div>
  <div class="ph skyline" role="img" aria-label="Line illustration of a city skyline"></div>
</section>

<div class="ph feat-photo" role="img" aria-label="Photo of a seaside resort pool with palm trees"></div>
<div class="abs h3" style="left:681px;top:1136px">FEATURES:</div>
<ul class="abs bullets" style="left:681px;top:1185px">
  <li>Travel 7 Days A Week</li>
  <li>Stay Your Choice Of Nights (1-4 Nights)</li>
  <li>Good For Two Adults &amp; Two Children</li>
  <li>Pay Just The Taxes &amp; Fees</li>
  <li>Multiple Travel Date Requests Allowed</li>
  <li>Fully Transferable To Another Person</li>
  <li>Just A 30 Days Advance Notice Required</li>
  <li>You Will Have 12 Months To Complete Travel</li>
</ul>

<section class="abs maroon">
  <div class="title">HOW CAN WE DO THIS?</div>
  <ul class="mlist" style="left:157px;top:160px;width:425px">
    <li>We contract with the world leading hotel chains and resorts to help them fill their otherwise empty rooms.</li>
    <li>We help fill empty rooms which the hotels, resorts and cruise lines turn into additional revenue from other areas of their property and future bookings.</li>
    <li>Hotels rarely experience full occupancy, yet they remain open, providing rooms and services at fixed costs. So when hotels give out their rooms by partnering with marketing companies like us, they might miss out on the room fee, but they already didn't have that in the first place, at least now they have the opportunity to gain a customer for their in-house restaurants, room service, their casinos, an extra day stay, future bookings, etc.</li>
  </ul>
  <div class="abs vrule"></div>
  <ul class="mlist" style="left:620px;top:160px;width:425px">
    <li>The magic of why our program works so well is the fact that it’s a win win for everyone involved. You win because you received a huge savings. The business who gave you the certificate wins because now you will remember them the next time you need the same kind of product or service that they provide and you might even refer your friends and family members. The hotels and resorts win because they gain additional revenue from other areas of their establishment that they otherwise would not have been able to get and they also have a new client that may book with them in the future. Remember, they didn’t have anyone in the room in the first place so since you are paying the normal rack rate you might be more inclined to spend your money at the hotel. You are never under any obligation to do so though!</li>
  </ul>
</section>
<div class="abs retail">
  <svg width="785" height="100" viewBox="0 0 785 100" aria-hidden="true"><polygon points="0,0 745,0 785,50 745,100 0,100" fill="#0c2d4e"/></svg>
  <div class="big">RETAIL VALUE: UP TO $826.00</div>
  <div class="small">(BASED ON $159.00 PER NIGHT)</div>
</div>

<div class="ph hiw-photo" role="img" aria-label="Photo of a resort terrace and pool at dusk"></div>
<div class="abs h3" style="left:681px;top:2216px">HOW IT WORKS</div>
<ul class="abs hiw" style="left:681px;top:2276px;width:366px">
  <li>You will receive up to 4 nights in a 3 star or better Las Vegas resort and casino for up to 4 travelers, 2 adults and 2 children.</li>
  <li>Simply redeem the certificate to activate the travel period for 1 year. This means you will have at least 1 year to travel from the date you redeem and activate your offer. Be sure to redeem your certificate before it expires! All certificates will have an accompanying expiration date attached to them.</li>
  <li>When you are ready to book you will simply have to pay the daily room rate taxes and fees of approximately $12-$33 per night (not per person). On average the taxes and fees come out to about $19 per night. (Retail Value: Up to $826.00 based on $159.00 per night)</li>
</ul>

<section class="abs testi">
  <div class="title"><span>CLIENT TESTIMONIAL</span></div>
</section>
<div class="card" style="left:157px;top:2844px;width:283px;height:232px">"I worked with the travel agency and they were very patient with me as I narrowed down where myself and another friend wanted to travel to. I gave them destinations and in return they gave me prompt responses on what was available and in our budget. Don't hesitate to work with this travel agency.....because I won't! "</div>
<div class="card" style="left:458px;top:2896px;width:283px;height:180px;padding-top:74px">"The travel agency did an excellent job booking my trip to Nashville. "</div>
<div class="card" style="left:758px;top:2844px;width:284px;height:232px;padding-top:32px">Wonderful! It was just like being in Rome, but only with great shows to enjoy. The rooms of the Grand Marquee and service were excellent. Going through the travel agency was simple and easy on the purse strings."</div>
<div class="who" style="left:216px;top:3106px"><b>MARCUS T.</b><br>Duluth, GA<br>Added on 01/21/2020 09:27:24 pm</div>
<div class="who" style="left:516px;top:3106px"><b>LEONARD K.</b><br>North Las Vegas, NV<br>Added on 01/21/2020 09:19:30 pm</div>
<div class="who" style="left:817px;top:3106px"><b>OWEN B.</b><br>Flagstaff, AZ<br>Added on 01/21/2020 09:03:06 pm</div>
<div class="dots"><i></i><i class="on"></i><i></i></div>

<div class="abs sell-title">HOW SELL THE PRODUCT</div>
<div class="ph video" role="img" aria-label="Video still of a rooftop resort pool with palm trees"></div>
<svg class="abs play" viewBox="0 0 96 96" aria-hidden="true"><polygon points="38,30 66,48 38,66" fill="#e0262b"/></svg>

<section class="abs steps">
  <div class="step" style="left:160px"><div class="n">1.</div><p>Redeem your certificate to activate<br>your offer</p></div>
  <div class="step" style="left:458px"><div class="n">2.</div><p>Fill out the online reservation request form with travel dates within the next 12 months.</p></div>
  <div class="step" style="left:767px"><div class="n">3.</div><p>Wait for a confirmation of your booked reservation. You will be notified immediately upon us booking your reservation.</p></div>
</section>

<div class="abs closing">
  <p>Go on your vacation and thank the business who gave you this special offer by doing business with them again and referring your friends and family members!</p>
  <h3>NO TIMESHARES OR SALES PRESENTATIONS,</h3>
  <h2>GUARANTEED!</h2>
</div>

<footer class="abs footer">
  <div class="fcol" style="left:157px;width:250px"><h5>HAVE QUESTIONS?</h5>We are here to help you redeem your certificates.Feel free to contact us with any questions or suggestions on how we can do our job better.</div>
  <div class="fcol" style="left:496px;width:265px"><h5>TERMS &amp; CONDITIONS</h5>long established fact that a reader will be distracted by the readable content of a page when looking at its layout.</div>
  <div class="fcol" style="left:823px;width:230px"><h5>CONTACT US</h5>
    <div style="display:flex;gap:10px"><svg width="12" height="16" viewBox="0 0 12 16" style="flex:none;margin-top:2px"><path d="M6 0 A6 6 0 0 1 12 6 C12 10 6 16 6 16 C6 16 0 10 0 6 A6 6 0 0 1 6 0Z" fill="#fff"/><circle cx="6" cy="6" r="2.3" fill="#0c2d4e"/></svg>
    <div>The Claims Desk<br>4120 Harmon Ridge Rd Ste B #210<br>Cedar Falls, Ca 90417</div></div>
  </div>
  <div class="abs frule"></div>
  <div class="abs copy">Copyright©2020 Bonus Gratuity Dispatch Network. All Rights Reserved.</div>
</footer>

</body>
</html>
```